High-End audio shop owner needs a business card

I need a personal Business Card for my Audio shop which exists since 1962. We offer high Quality brands, professional Attention and run our own repair-service-department. I look for a design which will be printed on high Quality paper and shall convey trust to the Client that we are very serious. Language is german.

```html
<!DOCTYPE html>
<html lang="de">
<head>
<meta charset="utf-8">
<title>Hi-Fi Lindenhof – Visitenkarte</title>
<link href="https://fonts.googleapis.com/css2?family=Roboto:wght@400;500;900&display=swap" rel="stylesheet">
<style>
  :root {
    --stage: #ffffff;
    --card-top: #1d1e20;
    --card-bottom: #0d0d0e;
    --orange: #f26522;
    --glow: #ffb36b;
    --text-light: #e8e8e8;
    --text-muted: #b9b9b9;
    --divider: #6a6a6a;
    --icon-glyph: #141414;
  }
  * { margin: 0; padding: 0; box-sizing: border-box; }
  html, body {
    width: 1200px; height: 900px; overflow: hidden;
    background: var(--stage);
    font-family: "Roboto", Arial, sans-serif;
  }
  .stage {
    position: relative; width: 1200px; height: 900px;
  }
  .card {
    position: absolute; top: 275px;
    width: 540px; height: 350px;
    border-radius: 24px;
    background: linear-gradient(160deg, var(--card-top), var(--card-bottom));
    overflow: hidden;
    box-shadow: 0 14px 30px rgba(0,0,0,0.22);
  }
  .card--front { left: 40px; }
  .card--back { left: 620px; }

  .brand-name {
    position: absolute;
    font-weight: 900;
    color: var(--orange);
    letter-spacing: 1px;
    white-space: nowrap;
    text-transform: uppercase;
  }
  .card--front .brand-name {
    top: 66px; left: 0; width: 100%; text-align: center; font-size: 34px;
  }
  .card--back .brand-name {
    top: 138px; left: 118px; font-size: 34px;
  }

  .soundwave {
    position: absolute; left: 0; top: 128px; width: 100%; height: 60px;
    background:
      linear-gradient(180deg, transparent 0%, rgba(242,101,34,0.35) 35%, var(--glow) 50%, rgba(242,101,34,0.35) 65%, transparent 100%);
  }

  .person {
    position: absolute; top: 208px; left: 60px; width: 170px; text-align: right;
  }
  .person__name { color: var(--orange); font-size: 16px; font-weight: 500; }
  .person__role { color: var(--text-muted); font-size: 13px; margin-top: 6px; }

  .divider {
    position: absolute; left: 252px; top: 196px; width: 1px; height: 118px;
    background: var(--divider);
  }

  .contacts {
    position: absolute; left: 270px; top: 194px; list-style: none;
  }
  .contacts li {
    display: flex; align-items: center; gap: 10px;
    height: 30px; color: var(--text-light); font-size: 14px;
  }
  .contacts svg { width: 18px; height: 18px; flex: none; }

  .speaker-stack {
    position: absolute; right: 0; top: 20px; width: 260px; height: 330px;
    background: linear-gradient(100deg, rgba(40,40,42,0) 0%, rgba(44,44,46,0.85) 45%, #222224 100%);
  }
</style>
</head>
<body>
<main class="stage">

  <section class="card card--front" aria-label="Vorderseite">
    <div class="brand-name">Hi-Fi Lindenhof</div>
    <div class="soundwave" role="img" aria-label="Leuchtende orange Schallwelle quer über die Karte"></div>

    <div class="person">
      <div class="person__name">Mara Feldmann</div>
      <div class="person__role">Manager</div>
    </div>
    <div class="divider"></div>

    <ul class="contacts">
      <li>
        <svg viewBox="0 0 18 18" aria-hidden="true"><circle cx="9" cy="9" r="9" fill="var(--orange)"/><path d="M6 4.5l2 2-1 1.3c.6 1.3 1.6 2.3 2.9 2.9l1.3-1 2 2-1.2 1.4C8.6 13 5 9.4 4.6 6z" fill="var(--icon-glyph)"/></svg>
        0301 52 64 18
      </li>
      <li>
        <svg viewBox="0 0 18 18" aria-hidden="true"><circle cx="9" cy="9" r="9" fill="var(--orange)"/><rect x="4.5" y="5.8" width="9" height="6.4" rx="1" fill="var(--icon-glyph)"/><path d="M4.8 6.2L9 9.3l4.2-3.1" stroke="var(--orange)" stroke-width="0.9" fill="none"/></svg>
        info@hifilindenhof.de
      </li>
      <li>
        <svg viewBox="0 0 18 18" aria-hidden="true"><circle cx="9" cy="9" r="9" fill="var(--orange)"/><g stroke="var(--icon-glyph)" stroke-width="1" fill="none"><circle cx="9" cy="9" r="4.5"/><ellipse cx="9" cy="9" rx="2" ry="4.5"/><path d="M4.5 9h9"/></g></svg>
        www.hifilindenhof.de
      </li>
      <li>
        <svg viewBox="0 0 18 18" aria-hidden="true"><circle cx="9" cy="9" r="9" fill="var(--orange)"/><path d="M9 3.8a3.4 3.4 0 0 0-3.4 3.4C5.6 9.8 9 14 9 14s3.4-4.2 3.4-6.8A3.4 3.4 0 0 0 9 3.8z" fill="var(--icon-glyph)"/><circle cx="9" cy="7.3" r="1.2" fill="var(--orange)"/></svg>
        Nr. 21, lindenstraße, berlin
      </li>
    </ul>
  </section>

  <section class="card card--back" aria-label="Rückseite">
    <div class="speaker-stack" role="img" aria-label="Dunkle Lautsprecherboxen und Subwoofer, gestapelt am rechten Rand"></div>
    <div class="brand-name">Hi-Fi Lindenhof</div>
  </section>

</main>
</body>
</html>
```